new pool company

I just started I pool service company last November based out of Winchester VA. My companies name is Brookstone Pool And Spa Service, LLC. I've been in the pool industry for 10 years. I want to build a customer base in my area.

I have an out of area telephone number so I want the postcard that I send out have something on it that lets people know I am a locally owned and operated company.

I also want it to say 'Licensed and Insured'

services provided (commercial and residential):
-Heater installs/diagnostics/repairs
-pool inspections
-electrical repairs
-plumbing repairs
-full system installations
-salt system conversions
-drain cleans w/ or w/ out acid
-pool closings
Lastly I want to feature the "pool openings" service on the card because that is the season that is coming.

The contact info I want displayed will be Kylemarsh@inboxly.example and my phone number at (555)-314-6027
Updates

I would like to see both side of the the card. I would also like pool openings to be more featured as a coming up service and not as a new service.

Must show both sides of card

Target Market(s)

I'm targeting upper middle class to upper class because of the obvious reasons of most pools are located in those areas.

Industry/Entity Type

Pool Service

Font styles to use
Serif
Sans Serif

Colors

Designer to choose colors to be used in the design.

Requirements
Must have
• Must have:
-Company name and contact info
-"Licensed and Insured"
-Logo that is attached
-"Locally owned and operated"

```html
<!DOCTYPE html>
<html lang="en">
<head>
<meta charset="utf-8">
<title>Brookstone Pool And Spa Service — Postcard</title>
<link href="https://fonts.googleapis.com/css2?family=Quicksand:wght@500;600&family=Roboto:ital,wght@0,700;1,500;1,700&display=swap" rel="stylesheet">
<style>
  :root {
    --page: #ecebe8;
    --white: #ffffff;
    --sky-top: #cfe3f3;
    --sky-mid: #9fc6e6;
    --pool-deep: #1f8fd0;
    --pool-light: #6cc4ea;
    --deck: #b9a996;
    --accent-blue: #52b8e6;
    --text-blue: #1a9fdc;
    --address-blue: #2a7fd0;
    --red: #e0231d;
    --seal-red: #e63b2e;
    --ribbon: #8fd3ef;
    --sun: #f7c326;
    --water-a: #3f9fe0;
    --water-b: #8fd1f4;
  }
  html, body {
    margin: 0;
    padding: 0;
    width: 759px;
    height: 1200px;
    overflow: hidden;
    background: var(--page);
  }
  .canvas { position: relative; width: 759px; height: 1200px; }

  .card {
    position: absolute;
    left: 47px;
    width: 664px;
    height: 514px;
    overflow: hidden;
    background: var(--white);
  }
  .card--front { top: 53px; }
  .card--back { top: 616px; }

  /* Front */
  .hero-photo {
    position: absolute; left: 0; top: 0; width: 664px; height: 423px;
    background: linear-gradient(180deg, var(--sky-top) 0%, var(--sky-mid) 30%, var(--deck) 42%, var(--pool-light) 55%, var(--pool-deep) 78%, var(--pool-light) 100%);
  }
  .header-strip {
    position: absolute; left: 0; top: 0; width: 664px; height: 125px;
    background: linear-gradient(180deg, rgba(255,255,255,0.35), rgba(255,255,255,0));
  }
  .brand-mark {
    position: absolute; left: 41px; top: 10px; width: 95px; height: 92px; background: var(--white);
  }
  .brand-mark__circle {
    position: absolute; left: 22px; top: 21px; width: 50px; height: 50px; border-radius: 50%; background: var(--sun);
  }
  .brand-name {
    position: absolute; left: 150px; top: 20px; margin: 0;
    font-family: "Quicksand", sans-serif; font-weight: 500; font-size: 28px; line-height: 35px;
    color: var(--white); text-transform: uppercase; letter-spacing: 0;
  }
  .brand-rule {
    position: absolute; left: 40px; top: 104px; width: 476px; height: 4px; background: var(--white); opacity: 0.85;
  }
  .seal { position: absolute; left: 521px; top: 12px; width: 110px; height: 110px; }
  .seal__text {
    position: absolute; left: 10px; top: 33px; width: 80px; margin: 0; text-align: center;
    font-family: "Roboto", sans-serif; font-style: italic; font-weight: 700; font-size: 10px; line-height: 14px;
    color: var(--white); text-transform: uppercase;
  }

  .contact-band {
    position: absolute; left: 0; top: 423px; width: 664px; height: 91px; background: var(--white);
  }
  .phone-icon { position: absolute; left: 36px; top: 18px; width: 56px; height: 56px; }
  .call-cta {
    position: absolute; left: 104px; top: 14px; margin: 0;
    font-family: "Quicksand", sans-serif; font-weight: 500; font-size: 32px; line-height: 30px;
    color: var(--accent-blue); text-transform: uppercase;
  }
  .band-divider { position: absolute; top: 0; width: 8px; height: 91px; background: var(--accent-blue); }
  .band-divider--a { left: 316px; }
  .band-divider--b { left: 330px; }
  .contact-details {
    position: absolute; left: 355px; top: 11px; margin: 0;
    font-family: "Roboto", sans-serif; font-style: italic; font-weight: 500; font-size: 21px; line-height: 34px;
    color: var(--text-blue);
  }

  /* Back */
  .water-backdrop {
    position: absolute; inset: 0;
    background: linear-gradient(160deg, var(--water-b) 0%, var(--water-a) 45%, var(--water-b) 80%, var(--water-a) 100%);
  }
  .services-tag {
    position: absolute; left: 16px; top: 21px; width: 333px; height: 66px;
    background: var(--white); border-radius: 33px 0 0 33px;
  }
  .services-tag__title {
    position: absolute; left: 37px; top: 10px; margin: 0;
    font-family: "Roboto", sans-serif; font-weight: 700; font-size: 21px; line-height: 24px;
    color: var(--red); text-transform: uppercase;
  }
  .services-tag__note {
    position: absolute; left: 37px; top: 35px; margin: 0;
    font-family: "Roboto", sans-serif; font-style: italic; font-weight: 700; font-size: 15px; line-height: 18px;
    color: var(--red);
  }
  .services-tag__circle {
    position: absolute; left: 272px; top: 10px; width: 46px; height: 46px; border-radius: 50%; background: var(--sun);
  }
  .services-panel {
    position: absolute; left: 16px; top: 115px; width: 406px; height: 344px;
    background: var(--white); border-radius: 30px;
  }
  .services-list {
    list-style: none; margin: 0; padding: 22px 0 0 20px;
    font-family: "Roboto", sans-serif; font-style: italic; font-weight: 500; font-size: 21px; line-height: 30px;
    color: var(--text-blue);
  }
  .services-list__upcoming { color: var(--red); padding-left: 44px; }
  .address-panel {
    position: absolute; left: 453px; top: 115px; width: 193px; height: 344px;
    background: var(--white); border-radius: 30px;
  }
  .address-lines {
    margin: 0; padding: 20px 0 0 20px;
    font-family: "Roboto", sans-serif; font-style: italic; font-weight: 500; font-size: 16px; line-height: 30px;
    color: var(--address-blue); text-transform: uppercase;
  }
</style>
</head>
<body>
<div class="canvas">

  <section class="card card--front" aria-label="Postcard front">
    <div class="hero-photo" role="img" aria-label="Photo of a sunlit rectangular backyard pool with a wooden deck and red lounge chairs"></div>
    <div class="header-strip"></div>
    <div class="brand-mark"><div class="brand-mark__circle"></div></div>
    <h1 class="brand-name">Brookstone Pool<br>And Spa Service, LLC</h1>
    <div class="brand-rule"></div>

    <div class="seal">
      <svg width="110" height="110" viewBox="0 0 110 110" aria-hidden="true">
        <polygon points="30,70 22,104 34,96 42,106 48,78" fill="var(--ribbon)"/>
        <polygon points="70,70 78,104 66,96 58,106 52,78" fill="var(--ribbon)"/>
        <circle cx="50" cy="46" r="44" fill="var(--white)"/>
        <circle cx="50" cy="46" r="37" fill="var(--seal-red)"/>
      </svg>
      <p class="seal__text">Licensed<br>&amp; Insured!</p>
    </div>

    <div class="contact-band">
      <svg class="phone-icon" viewBox="0 0 24 24" aria-hidden="true">
        <path fill="var(--accent-blue)" d="M6.6 10.8c1.4 2.8 3.8 5.1 6.6 6.6l2.2-2.2c.3-.3.7-.4 1-.2 1.1.4 2.3.6 3.6.6.6 0 1 .4 1 1V20c0 .6-.4 1-1 1C10.6 21 3 13.4 3 4c0-.6.4-1 1-1h3.5c.6 0 1 .4 1 1 0 1.3.2 2.5.6 3.6.1.3 0 .7-.2 1z"/>
      </svg>
      <p class="call-cta">Call Kyle<br>Now!</p>
      <div class="band-divider band-divider--a"></div>
      <div class="band-divider band-divider--b"></div>
      <p class="contact-details">(555)-314-6027<br>Kylemarsh@inboxly.example</p>
    </div>
  </section>

  <section class="card card--back" aria-label="Postcard back">
    <div class="water-backdrop" role="img" aria-label="Rippling clear blue pool water"></div>

    <div class="services-tag">
      <p class="services-tag__title">Services Provided</p>
      <p class="services-tag__note">(commercial and residential):</p>
      <div class="services-tag__circle"></div>
    </div>

    <div class="services-panel">
      <ul class="services-list">
        <li>Heater installs/diagnostics/repairs</li>
        <li>-pool inspections</li>
        <li>-electrical repairs</li>
        <li>-plumbing repairs</li>
        <li>-full system installations</li>
        <li>-salt system conversions</li>
        <li>-drain cleans w/ or w/ out acid</li>
        <li>-pool closings</li>
        <li class="services-list__upcoming">COMING UP: pool openings</li>
      </ul>
    </div>

    <div class="address-panel">
      <p class="address-lines">Address Line 1<br>Address Line 2<br>Address Line 3<br>Address Lne 4</p>
    </div>
  </section>

</div>
</body>
</html>
```